A new customer-driven VC fund for Enterprise IT Startups

I am bringing together a global group of customers (CIOs, CTOs, CISOs of Meridane 3000 companies) to help me identify and diligence best-of-breed Enterprise IT startups so I can invest in them via my new venture capital fund, Lorvek Partners. In many ways, this is a new model for a VC fund and my goal is to revolutionize Venture Capital so that we hit the bull's eye in investing way more often in what is otherwise a guessing game for most VCs. So in the website, I'd like to capture the essences of global reach, best-of-breed, breakthrough innovation. I also want it to convey the ability of Lorvek Partners to create category winners (i.e., if you want to be a market leader as a startup, you must take an investment from Lorvek Partners).
My current website is www.lorvek-partners.example - please use the content from the website within your design but please DO NOT use the design elements from the current website. INSTEAD, I'm looking for new and creative ideas on how I can leverage the existing content in a more appealing design -- any designs that look remotely similar to the existing website will be immediately declined.
I also want to ensure that the web design is mobile friendly.
Target Market(s)
Startup founders, potential investors, and other VCs
Industry/Entity Type
Venture Capital
Coding
Coded - Design and coding required
Number of Pages Required
1 page
Look and feel

```html
<!DOCTYPE html>
<html lang="en">
<head>
<meta charset="utf-8">
<title>Lorvek Partners — Venture Capital for Enterprise IT</title>
<link href="https://fonts.googleapis.com/css2?family=Source+Sans+3:ital,wght@0,300;0,400;0,600;0,700;1,400&display=swap" rel="stylesheet">
<style>
:root{
  --navy:#005799;
  --blue:#337bb0;
  --light:#f0f5f9;
  --ink:#3d4a57;
  --muted:#7b8794;
  --line:#e2e8ee;
  --white:#ffffff;
}
*{box-sizing:border-box;margin:0;padding:0}
html,body{width:1200px;height:3744px;overflow:hidden}
body{font-family:"Source Sans 3",sans-serif;color:var(--ink);background:var(--white)}
.page{position:relative;width:1200px;height:3744px;overflow:hidden}
.abs{position:absolute}
.eyebrow{font-size:10px;letter-spacing:5px;text-transform:uppercase;color:var(--muted)}
.title{font-size:32px;font-weight:600;color:var(--navy)}
.title b{font-weight:700}
.body{font-size:13px;line-height:24px;color:var(--ink)}

/* hero */
.hero{left:0;top:0;width:1200px;height:677px;background:linear-gradient(120deg,#2e5d8f 0%,#4a7fb3 45%,#6f9cc8 70%,#3e6e9f 100%)}
.nav{left:162px;top:25px;width:880px;height:72px;border-radius:36px;background:rgba(255,255,255,.32);display:flex;align-items:center;padding:0 12px 0 40px}
.brand{font-size:22px;font-weight:700;color:var(--white);display:flex;align-items:center;gap:10px}
.brand i{width:14px;height:14px;border-radius:50%;background:var(--white);display:inline-block}
.menu{display:flex;gap:0;margin-left:auto;margin-right:auto;font-size:10px;color:var(--white);letter-spacing:.5px}
.menu span{padding:0 18px;border-left:1px solid rgba(255,255,255,.6)}
.menu span:first-child{border-left:none}
.phone{width:56px;height:56px;border-radius:50%;background:var(--navy);display:flex;align-items:center;justify-content:center;box-shadow:0 0 0 5px rgba(255,255,255,.5)}
.hero h1{left:162px;top:292px;font-size:40px;line-height:52px;font-weight:700;color:var(--white)}
.hero p{left:162px;top:400px;width:720px;font-size:14px;line-height:27px;color:var(--white)}
.down{left:162px;top:520px;width:64px;height:64px;border-radius:50%;border:2px solid rgba(255,255,255,.8);background:rgba(80,140,200,.5);display:flex;align-items:center;justify-content:center}
.tab{left:687px;top:629px;width:342px;height:97px;background:var(--blue);color:var(--white);font-size:17px;font-weight:600;display:flex;align-items:center;justify-content:center;box-shadow:0 10px 30px rgba(0,60,110,.25);z-index:2}

/* who */
.who{left:0;top:677px;width:1200px;height:449px;background:linear-gradient(180deg,var(--light),#e9f0f6)}
.btn{display:inline-flex;align-items:center;justify-content:center;width:112px;height:40px;border-radius:20px;background:var(--blue);color:var(--white);font-size:10px;font-weight:600;letter-spacing:.5px}
.links{font-style:italic;color:var(--blue);font-size:14px;line-height:24px}
.links u{text-decoration:underline}
.who-art{left:687px;top:116px;width:300px;height:281px;border-radius:50%;background:radial-gradient(circle at 50% 45%,#ffffff 0%,#dbe6ef 60%,#c3d3e1 100%)}

/* numbers */
.nums-band{left:0;top:1126px;width:601px;height:450px;background:var(--navy)}
.handshake{left:162px;top:1287px;width:439px;height:358px;background:linear-gradient(160deg,#e8eef3 0%,#c9d3dc 55%,#4b5563 100%)}
.stat{left:687px;width:353px;border-bottom:1px solid var(--line);padding-bottom:14px}
.stat .n{font-size:44px;font-weight:700;line-height:48px;color:transparent;-webkit-text-stroke:1.4px var(--blue)}
.stat .l{font-size:10px;color:var(--muted);margin-top:2px}

/* cards */
.card{width:292px;background:var(--white);border:1px solid var(--line);padding:58px 34px 0}
.card h3{font-size:14px;font-weight:700;color:var(--navy);margin-bottom:10px}
.card p{font-size:10.5px;line-height:22px;color:var(--ink)}
.ico{width:62px;height:62px;border-radius:50%;background:var(--navy);display:flex;align-items:center;justify-content:center;box-shadow:0 0 0 5px rgba(0,87,153,.12)}

/* engine */
.eng-band{left:601px;top:2132px;width:599px;height:451px;background:var(--blue)}
.eng-photo{left:601px;top:2293px;width:439px;height:358px;background:linear-gradient(150deg,#c8d4df 0%,#9fb3c6 40%,#6c87a2 75%,#8ea6bd 100%)}
.feat h4{font-size:14px;font-weight:700;color:var(--navy);margin-bottom:8px}
.feat p{font-size:10.5px;line-height:21px;color:var(--ink);width:360px}

/* focus */
.focus{left:162px;top:2807px;width:878px;display:flex;justify-content:space-between}
.area{width:130px;text-align:center}
.area svg{display:block;margin:0 auto 8px}
.area span{display:block;border:1px solid var(--line);font-size:9px;color:var(--navy);padding:10px 0}

/* team */
.team{left:0;top:2950px;width:1200px;height:682px;background:var(--light)}
.grid{left:162px;top:175px;width:878px;display:grid;grid-template-columns:repeat(4,201px);column-gap:24.6px;row-gap:20px}
.member{height:207px;background:var(--white);text-align:center;padding-top:28px}
.avatar{width:92px;height:92px;border-radius:50%;margin:0 auto 12px;border:2px solid #d8e3ec;background:linear-gradient(180deg,#dfe7ee 0%,#a9b9c8 100%)}
.member b{display:block;font-size:11px;color:var(--navy);font-weight:700}
.member em{display:block;font-size:8.5px;color:var(--muted);margin-top:3px}

/* footer */
.footer{left:0;top:3632px;width:1200px;height:112px;background:var(--navy);display:flex;align-items:center;padding:0 162px}
.footer .copy{margin-left:auto;margin-right:auto;font-size:9px;color:var(--white);padding-left:60px}
.social{display:flex;gap:10px}
.social i{width:10px;height:10px;border-radius:50%;background:var(--white);display:block}
</style>
</head>
<body>
<div class="page">

  <!-- Hero -->
  <section class="hero abs" role="img" aria-label="Photo of a businessperson working at a laptop on a desk with coffee cups, tinted blue">
  </section>
  <nav class="nav abs">
    <div class="brand"><i></i>Lorvek Partners</div>
    <div class="menu"><span>ABOUT</span><span>NETWORK</span><span>GTM ENGINE</span><span>TEAM &amp; ADVISORS</span></div>
    <div class="phone">
      <svg width="22" height="22" viewBox="0 0 24 24" fill="none" stroke="#fff" stroke-width="2" stroke-linecap="round" stroke-linejoin="round"><path d="M22 16.9v3a2 2 0 0 1-2.2 2 19.8 19.8 0 0 1-8.6-3.1 19.5 19.5 0 0 1-6-6A19.8 19.8 0 0 1 2.1 4.2 2 2 0 0 1 4.1 2h3a2 2 0 0 1 2 1.7c.1 1 .4 1.9.7 2.8a2 2 0 0 1-.5 2.1L8 9.9a16 16 0 0 0 6 6l1.3-1.3a2 2 0 0 1 2.1-.4c.9.3 1.8.6 2.8.7a2 2 0 0 1 1.7 2z"/></svg>
    </div>
  </nav>
  <h1 class="abs" style="left:162px;top:292px;font-size:40px;line-height:52px;font-weight:700;color:#fff">We Invest in Enterprise IT Startups<br>at the Product-Market-Fit Stage</h1>
  <p class="abs" style="left:162px;top:400px;width:720px;font-size:14px;line-height:27px;color:#fff">We are singularly focused on helping our portfolio companies gain a massive competitive advantage by providing them access to our exclusive network of hundreds of early-adopting CIOs, CTOs, CISOs, and Channel Partners around the world to rapidly accelerate customer traction.</p>
  <div class="down abs">
    <svg width="20" height="20" viewBox="0 0 24 24" fill="none" stroke="#fff" stroke-width="2" stroke-linecap="round"><path d="M12 4v16M6 14l6 6 6-6"/></svg>
  </div>
  <div class="tab abs">Venture Capital Investments</div>

  <!-- Who we are -->
  <section class="who abs">
    <div class="eyebrow abs" style="left:162px;top:128px">Introduction</div>
    <h2 class="title abs" style="left:162px;top:146px">Who We Are</h2>
    <p class="body abs" style="left:162px;top:196px;width:330px">We only invest in post-product, post-revenue Enterprise IT startups. Usually, this means you're at Seed Extension to Series A stage.</p>
    <p class="links abs" style="left:162px;top:278px">Want to be a market leader as a startup?<br>Take an investment from <u>Lorvek Partners</u></p>
    <a class="btn abs" style="left:162px;top:358px">CONTACT US</a>
    <div class="who-art abs" role="img" aria-label="Circular collage of business photos suggesting global reach and upward growth"></div>
  </section>

  <!-- Strength in numbers -->
  <div class="nums-band abs"></div>
  <div class="eyebrow abs" style="left:162px;top:1191px;color:#cfe0ee">GTM in Numbers</div>
  <h2 class="abs" style="left:162px;top:1212px;font-size:32px;font-weight:400;color:#fff">Strength <b style="font-weight:700">in Numbers</b></h2>
  <div class="handshake abs" role="img" aria-label="Photo of two businessmen in suits shaking hands in a bright office"></div>
  <p class="abs" style="left:687px;top:1208px;width:353px;font-size:12.5px;line-height:24px;font-style:italic">We collect and analyze monthly purchase intent data from a global network of IT decision makers.</p>
  <div class="stat abs" style="top:1290px"><div class="n">500+</div><div class="l">Early adopting, influential CIOs, CTOs, CISOs and IT decision makers</div></div>
  <div class="stat abs" style="top:1380px"><div class="n">$100B+</div><div class="l">Annual enterprise technology purchasing budget across our network</div></div>
  <div class="stat abs" style="top:1470px"><div class="n">15</div><div class="l">Countries represented in our current network</div></div>
  <div class="stat abs" style="top:1560px;border-bottom:none"><div class="n">550+</div><div class="l">Purchase intent data points collected monthly</div></div>

  <!-- Value cards -->
  <div class="card abs" style="left:162px;top:1819px;height:232px">
    <div class="ico abs" style="left:34px;top:-31px">
      <svg width="28" height="28" viewBox="0 0 24 24" fill="none" stroke="#fff" stroke-width="1.8" stroke-linecap="round" stroke-linejoin="round"><path d="M2 12l4-4 4 2 3-2 3 2 4-1 2 3-6 5-3-2-3 2z"/></svg>
    </div>
    <h3>Customers</h3>
    <p>Hundreds of earliest-adopting CIOs, CTOs, and CISOs from Meridane 3000 to Global 2000 to Cloud-First companies are a part of our exclusive network.</p>
  </div>
  <div class="card abs" style="left:454px;top:1780px;height:241px">
    <div class="ico abs" style="left:34px;top:-31px">
      <svg width="26" height="26" viewBox="0 0 24 24" fill="none" stroke="#fff" stroke-width="2.2" stroke-linecap="round"><circle cx="10" cy="10" r="6"/><path d="M15 15l6 6"/></svg>
    </div>
    <h3>Our Investment Philosophy</h3>
    <p>We only invest in startups that have broad &amp; immediate applicability across a global CIO base and are solving critical problems. To give our portfolio companies a truly unfair competitive advantage, we do not invest in competitive startups.</p>
  </div>
  <div class="card abs" style="left:746px;top:1753px;height:236px">
    <div class="ico abs" style="left:34px;top:-31px">
      <svg width="28" height="28" viewBox="0 0 24 24" fill="#fff"><circle cx="8" cy="7" r="3"/><circle cx="16" cy="7" r="3"/><path d="M2 20c0-4 3-7 6-7s6 3 6 7zM12 20c0-3 1.5-5 4-6 3 0 6 3 6 6z"/></svg>
    </div>
    <h3>Customer-Led Investments</h3>
    <p>A global roster of CIOs leads our investment decision-making process. We also share candid, unfiltered feedback from dozens of customers via a Lorvek Memo™ with every single startup who presents to us – even if we don't end up investing.</p>
  </div>

  <!-- GTM engine -->
  <div class="eng-band abs"></div>
  <div class="eyebrow abs" style="left:687px;top:2210px;color:#cfe0ee">What We Are</div>
  <h2 class="abs" style="left:687px;top:2230px;font-size:30px;font-weight:400;color:#fff">A Global <b style="font-weight:700">GTM ENGINE</b></h2>
  <div class="eng-photo abs" role="img" aria-label="Photo of businesspeople around a laptop with a rising growth chart overlay"></div>
  <p class="abs" style="left:162px;top:2205px;width:360px;font-size:11px;line-height:24px">We don't just make "customer intros", we partner with you each step of the way to help you navigate the complex landscape of enterprise sales, from key strategic accounts to strategic channel partners.</p>
  <div class="feat abs" style="left:162px;top:2326px"><h4>GTM Coaches</h4><p>We will partner with you to navigate the complex enterprise sales process by leveraging our executive network to provide product feedback, sales strategy, and market insights.</p></div>
  <div class="feat abs" style="left:162px;top:2453px"><h4>Strategic Partners</h4><p>Strategic partnerships can propel a startup to the next level. Leverage our extensive network of IT Executives, Channel Partners, and OEMs to accelerate your path to becoming a category leader.</p></div>
  <div class="feat abs" style="left:162px;top:2579px"><h4>Global Ambassadors</h4><p>Expanding globally is no simple exercise. Our network of Global IT Execs will provide on-the-ground intelligence, referrals, and influence as you conquer new geographies.</p></div>

  <!-- Focus areas -->
  <div class="eyebrow abs" style="left:0;width:1200px;text-align:center;top:2728px">How We Invest</div>
  <h2 class="abs" style="left:0;width:1200px;text-align:center;top:2745px;font-size:28px;font-weight:400;color:var(--navy)">Investment <b style="font-weight:700">Focus Areas</b></h2>
  <div class="focus abs">
    <div class="area"><svg width="30" height="30" viewBox="0 0 24 24" fill="var(--blue)"><path d="M12 2l8 3v6c0 5-3.5 9-8 11-4.5-2-8-6-8-11V5z"/><path d="M8 12l3 3 5-6" stroke="#fff" stroke-width="2" fill="none"/></svg><span>Security</span></div>
    <div class="area"><svg width="30" height="30" viewBox="0 0 24 24" fill="var(--blue)"><circle cx="12" cy="12" r="9"/><path d="M12 4v16M8 8h4M12 15h4M8 12h-3" stroke="#fff" stroke-width="1.6"/></svg><span>AI &amp; ML</span></div>
    <div class="area"><svg width="30" height="30" viewBox="0 0 24 24" fill="var(--blue)" stroke="var(--blue)" stroke-width="1.5"><circle cx="12" cy="12" r="2.5"/><circle cx="4" cy="4" r="2"/><circle cx="20" cy="4" r="2"/><circle cx="4" cy="20" r="2"/><circle cx="20" cy="20" r="2"/><path d="M4 4l16 16M20 4L4 20"/></svg><span>Network &amp; Architecture</span></div>
    <div class="area"><svg width="30" height="30" viewBox="0 0 24 24" fill="var(--blue)"><path d="M7 18a5 5 0 0 1-.5-10A6 6 0 0 1 18 9a4.5 4.5 0 0 1-.5 9z"/><path d="M9 18v-5M12 18v-7M15 18v-4" stroke="#fff" stroke-width="1.5"/></svg><span>Cloud &amp; Infrastructure</span></div>
    <div class="area"><svg width="30" height="30" viewBox="0 0 24 24" fill="none" stroke="var(--blue)" stroke-width="2.2"><path d="M12 12c-2-3-4-4-6-4a4 4 0 0 0 0 8c2 0 4-1 6-4s4-4 6-4a4 4 0 0 1 0 8c-2 0-4-1-6-4z"/></svg><span>DevOps</span></div>
    <div class="area"><svg width="30" height="30" viewBox="0 0 24 24" fill="var(--blue)"><path d="M6 19a5 5 0 0 1-.5-10A6.5 6.5 0 0 1 18 10a4.5 4.5 0 0 1 0 9z"/><text x="12" y="16.5" font-size="5.5" font-family="Source Sans 3, sans-serif" font-weight="700" fill="#fff" text-anchor="middle">SaaS</text></svg><span>SAAS</span></div>
  </div>

  <!-- Team -->
  <section class="team abs">
    <div class="eyebrow abs" style="left:162px;top:82px">Meet Our Members</div>
    <h2 class="title abs" style="left:162px;top:100px;font-weight:700">Team, Investors &amp; Advisors</h2>
    <p class="abs" style="left:687px;top:76px;width:353px;font-size:12px;line-height:22px;font-style:italic">We have built a world-class roster of executive advisors and mentors with exceptional go-to-market pedigrees to help our portfolio companies in their go-to-market journeys.</p>
    <div class="grid abs">
      <div class="member"><div class="avatar" role="img" aria-label="Portrait photo"></div><b>Rafiq D. Omaru</b><em>Founder &amp; Managing Director</em></div>
      <div class="member"><div class="avatar" role="img" aria-label="Portrait photo"></div><b>Conrad Hale</b><em>Founder &amp; Ex-CEO, Quelvar</em></div>
      <div class="member"><div class="avatar" role="img" aria-label="Portrait photo"></div><b>Navin Sethar</b><em>Co-founder, Stratonyx CPO, Brinlo</em></div>
      <div class="member"><div class="avatar" role="img" aria-label="Portrait photo"></div><b>Tarik Solan</b><em>Co-founder, Pallaxa CEO</em></div>
      <div class="member"><div class="avatar" role="img" aria-label="Portrait photo"></div><b>Tobias Kren</b><em>President, Vantiel</em></div>
      <div class="member"><div class="avatar" role="img" aria-label="Portrait photo"></div><b>Joel Varga</b><em>Executive Director, Corvane</em></div>
      <div class="member"><div class="avatar" role="img" aria-label="Portrait photo"></div><b>Prof. Karim Lastow</b><em>Leading Crowdsourcing Expert</em></div>
      <div class="member"><div class="avatar" role="img" aria-label="Portrait photo"></div><b>Prof. Miles Berenholt</b><em>Human Computer Interaction Expert</em></div>
    </div>
  </section>

  <!-- Footer -->
  <footer class="footer abs">
    <div class="brand" style="font-size:20px"><i></i>Lorvek Partners</div>
    <div class="copy">Copyright © 2022 Lorvek Partners - All Rights Reserved.</div>
    <div class="social"><i></i><i></i></div>
  </footer>

</div>
</body>
</html>
```